Small Creativity Consulting Business Needs Annual Report Design

I need interior e-print design for a 14-page digital annual report to go out to our consumers and audiences (@3000 people). I have a small creativity consulting business that provides consulting services, programs, keynotes, and products designed to helped creative people be more productive and productive people be more creative. The report should not feel corporate but instead should feel consistent with the brand - Gathering Lantern - like a well-crafted field guide. Colors should be consistent with the burnt orange, deep red, and green used in our existing branding.
Burnt red color: 691419
Orange color: CF7019
Green color: 64600D

The final design should convey wonder mixed with wisdom and sound entrepreneurial guidance.

Target Market(s)

women & men, 30s-60s, who love creativity, the arts, books + who want to create & produce

Industry/Entity Type

Digital

Requirements
Must have
• The report should not feel corporate but instead should feel consistent with the brand - Gathering Lantern - like a well-crafted field guide. Colors should be consistent with the burnt orange, deep red, and green used in our existing branding.
Burnt red color: 691419
Orange color: CF7019
Green color: 64600D

It should include many of the photos we have attached.

Nice to have
• You might play on the Harrowgate Viaduct image toward the end.
Should not have
• Don't aim for "cute" or "jazzy" creative. We're a more subdued creativity brand - although "bold" is good.

```html
<!DOCTYPE html>
<html lang="en">
<head>
<meta charset="utf-8">
<title>Gathering Lantern Annual Report — Table of Contents</title>
<link rel="stylesheet" href="https://fonts.googleapis.com/css2?family=Cormorant+Unicase:wght@500;600&family=Old+Standard+TT&display=swap">
<style>
  :root {
    --burnt-red: #691419;
    --orange: #cf7019;
    --green: #64600d;
    --paper: #ffffff;
    --ground: #ffffff;
  }
  * { margin: 0; padding: 0; box-sizing: border-box; }
  html, body {
    width: 1200px;
    height: 1000px;
    overflow: hidden;
    background: var(--ground);
  }
  .page {
    position: absolute;
    left: 302px;
    top: 79px;
    width: 595px;
    height: 842px;
    background: var(--paper);
    overflow: hidden;
  }
  .contents-title {
    position: absolute;
    left: 75px;
    top: 128px;
    font-family: "Old Standard TT", serif;
    font-size: 17px;
    letter-spacing: 0.2px;
    color: var(--burnt-red);
    font-weight: 400;
  }
  .contents-list {
    position: absolute;
    left: 75px;
    top: 188px;
    width: 440px;
    list-style: none;
  }
  .contents-entry {
    display: flex;
    align-items: baseline;
    height: 42px;
    font-family: "Cormorant Unicase", serif;
    font-weight: 600;
    font-size: 22px;
    color: var(--orange);
    white-space: nowrap;
  }
  .entry-leader {
    flex: 1;
    overflow: hidden;
    margin: 0 3px;
    font-size: 17px;
    letter-spacing: 2.6px;
  }
  .entry-leader::before {
    content: ". . . . . . . . . . . . . . . . . . . . . . . . . . . . . . . . . . . . . . . . . . . . . . . . . . . . . . . . . . . . . . . . .";
  }
  .entry-page {
    font-size: 19px;
  }
  .tree-art {
    position: absolute;
    left: 14px;
    top: 452px;
    width: 566px;
    height: 390px;
  }
</style>
</head>
<body>
  <main class="page">
    <h1 class="contents-title">TABLE OF CONTENTS</h1>
    <ol class="contents-list">
      <li class="contents-entry"><span class="entry-name">You Are Here</span><span class="entry-leader"></span><span class="entry-page">2</span></li>
      <li class="contents-entry"><span class="entry-name">The Entrepreneur Serves the Creative</span><span class="entry-leader"></span><span class="entry-page">3</span></li>
      <li class="contents-entry"><span class="entry-name">Deep Create Zone</span><span class="entry-leader"></span><span class="entry-page">5</span></li>
      <li class="contents-entry"><span class="entry-name">Engaging My Packs</span><span class="entry-leader"></span><span class="entry-page">9</span></li>
      <li class="contents-entry"><span class="entry-name">My Father</span><span class="entry-leader"></span><span class="entry-page">12</span></li>
    </ol>
    <svg class="tree-art" viewBox="0 0 566 390" role="img" aria-label="Mirrored silhouette of a spreading tree in olive green, trunks rising from the bottom edge">
      <defs>
        <radialGradient id="canopy-tone" cx="50%" cy="55%" r="60%">
          <stop offset="0%" stop-color="#64600d" stop-opacity="0.85"/>
          <stop offset="70%" stop-color="#64600d" stop-opacity="0.35"/>
          <stop offset="100%" stop-color="#64600d" stop-opacity="0"/>
        </radialGradient>
      </defs>
      <rect x="0" y="0" width="566" height="390" fill="url(#canopy-tone)"/>
    </svg>
  </main>
</body>
</html>
```